Blue Heron IT Business Card - Clean, Simple

Need a simple, clean standard sized business card for an IT consulting business using existing logo and company colours. Background should be mainly white. Feel free to be creative but clean, simple, quiet design is preferred. Font is specified in logo but any sans serif fonts work.

Contact Information for card is as follows (doesn't need to be in this exact order):

Martin Calloway
Owner
martin@blueheronit.ca
705-391-2586
www.blueheronit.ca

Target Market(s)

Small to medium sized business.

Industry/Entity Type

IT Consulting

Contact Information for Business Card

Logo and contact info.

Font styles to use
Sans Serif

Colors
EE7325
F08F49
F5BC92
FAE3D3
FDF4ED

Requirements
Must have
• All white or mostly white background.

```html
<!DOCTYPE html>
<html lang="en">
<head>
<meta charset="utf-8">
<title>Blue Heron IT – Business Card</title>
<link rel="stylesheet" href="https://fonts.googleapis.com/css2?family=Open+Sans:wght@400;600;700&display=swap">
<style>
  :root {
    --orange: #EE7325;
    --orange-soft: #F08F49;
    --ink: #1d1d1d;
    --paper: #f6f6f6;
    --card-dark: #2b2b2b;
    --mark-dark: #1e1e1e;
    --backdrop: #e7e7e7;
  }
  * { box-sizing: border-box; margin: 0; padding: 0; }
  html, body {
    width: 1200px; height: 780px; overflow: hidden;
    background: var(--backdrop);
    font-family: "Open Sans", Arial, sans-serif;
  }
  .canvas {
    position: relative; width: 1200px; height: 780px;
    display: flex; align-items: center; justify-content: center; gap: 40px;
  }
  .card {
    position: relative; width: 540px; height: 309px; overflow: hidden;
    box-shadow: 0 8px 24px rgba(0,0,0,.18);
  }
  .card--front { background: var(--paper); }
  .card--back { background: var(--card-dark); }

  .front-swoosh { position: absolute; inset: 0; width: 100%; height: 100%; }

  .person { position: absolute; left: 34px; top: 70px; text-align: right; }
  .person__name { font-size: 22px; font-weight: 700; color: var(--ink); letter-spacing: .2px; }
  .person__name .first { color: var(--orange); }
  .person__role { font-size: 13px; font-weight: 400; color: var(--ink); margin-top: 2px; }

  .brand {
    position: absolute; display: flex; align-items: center; gap: 10px;
  }
  .brand__dot { width: 20px; height: 20px; border-radius: 50%; background: var(--orange); }
  .brand__name { font-weight: 700; letter-spacing: -.5px; }
  .card--front .brand { left: 262px; top: 60px; }
  .card--front .brand__name { font-size: 32px; color: var(--ink); }
  .card--back .brand { left: 50%; top: 50%; transform: translate(-50%, -50%); }
  .card--back .brand__name { font-size: 44px; color: var(--mark-dark); }

  .divider {
    position: absolute; left: 232px; top: 150px; width: 2px; height: 88px; background: var(--ink);
  }
  .contact { position: absolute; left: 250px; top: 152px; list-style: none; }
  .contact__item {
    display: flex; align-items: center; gap: 9px;
    font-size: 14px; color: var(--ink); line-height: 26px;
  }
  .contact__icon { width: 14px; height: 14px; flex: none; }
</style>
</head>
<body>
<main class="canvas">

  <section class="card card--front" aria-label="Business card front">
    <svg class="front-swoosh" viewBox="0 0 540 309" preserveAspectRatio="none" aria-hidden="true">
      <path d="M0 150 C 60 235 220 292 540 300 L540 309 L0 309 Z" fill="var(--orange)"/>
      <path d="M0 140 C 62 225 220 280 540 292 L540 300 C 220 292 60 235 0 150 Z" fill="var(--paper)"/>
      <path d="M30 150 C 95 225 240 270 490 283" fill="none" stroke="var(--ink)" stroke-width="3" stroke-linecap="round"/>
    </svg>

    <div class="brand">
      <span class="brand__dot"></span>
      <span class="brand__name">Blue Heron IT</span>
    </div>

    <div class="person">
      <p class="person__name"><span class="first">Martin</span> Calloway</p>
      <p class="person__role">Owner</p>
    </div>

    <div class="divider"></div>

    <ul class="contact">
      <li class="contact__item">
        <svg class="contact__icon" viewBox="0 0 24 24" aria-hidden="true"><path fill="var(--orange)" d="M6.6 10.8a15.1 15.1 0 0 0 6.6 6.6l2.2-2.2a1 1 0 0 1 1-.25 11.4 11.4 0 0 0 3.6.57 1 1 0 0 1 1 1V20a1 1 0 0 1-1 1A17 17 0 0 1 3 4a1 1 0 0 1 1-1h3.5a1 1 0 0 1 1 1c0 1.25.2 2.45.57 3.57a1 1 0 0 1-.25 1z"/></svg>
        <span>705-391-2586</span>
      </li>
      <li class="contact__item">
        <svg class="contact__icon" viewBox="0 0 24 24" aria-hidden="true"><circle cx="12" cy="12" r="10" fill="none" stroke="var(--orange)" stroke-width="2.4"/><path d="M2 12h20M12 2c3 3 3 17 0 20M12 2c-3 3-3 17 0 20" fill="none" stroke="var(--orange)" stroke-width="2"/></svg>
        <span>www.blueheronit.ca</span>
      </li>
      <li class="contact__item">
        <svg class="contact__icon" viewBox="0 0 24 24" aria-hidden="true"><rect x="2" y="5" width="20" height="14" rx="2" fill="var(--orange)"/><path d="M3 6l9 7 9-7" fill="none" stroke="#fff" stroke-width="2"/></svg>
        <span>martin@blueheronit.ca</span>
      </li>
    </ul>
  </section>

  <section class="card card--back" aria-label="Business card back">
    <div class="brand">
      <span class="brand__dot"></span>
      <span class="brand__name">Blue Heron IT</span>
    </div>
  </section>

</main>
</body>
</html>
```